Quorvex business card design

create modern and tech looking business card that is clean but effectively communciates that we are a cloud communications company.
Should have at minimum:
Employee Name
Postion
Phone Number
Email
website
create modern and tech looking business card that is clean but effectively communciates that we are a cloud communications company. We have two logo color schemes (attached) so would like to see designs both ways
Should have at minimum:
Employee Name
Postion
Phone Number
Email
website

```html
<!DOCTYPE html>
<html lang="en">
<head>
<meta charset="utf-8">
<title>Quorvex business card</title>
<link rel="stylesheet" href="https://fonts.googleapis.com/css2?family=Roboto:wght@400;500&family=Roboto+Condensed:wght@400;500&display=swap">
<style>
  :root {
    --backdrop: #2b2b2b;
    --card-white: #f3f3f3;
    --cyan: #2bb6d6;
    --purple: #5f2d87;
    --ink: #454545;
    --ink-soft: #555555;
    --white: #ffffff;
    --muted-white: #e6ddef;
  }
  * { margin: 0; padding: 0; box-sizing: border-box; }
  html, body {
    width: 1200px; height: 960px; overflow: hidden;
    background: var(--backdrop);
    font-family: "Roboto", Arial, sans-serif;
  }
  .canvas { position: relative; width: 1200px; height: 960px; }

  .card {
    position: absolute; width: 600px; height: 343px; overflow: hidden;
  }
  .card-front { left: 314px; top: 113px; background: var(--card-white); }
  .card-back { left: 311px; top: 472px; background: var(--purple); }

  .corner-shape { position: absolute; left: 0; top: 0; }

  .brand {
    position: absolute; display: flex; align-items: center; gap: 14px;
  }
  .brand-front { left: 42px; top: 66px; }
  .brand-mark { width: 22px; height: 22px; background: var(--purple); }
  .brand-name {
    font-family: "Roboto", Arial, sans-serif; font-weight: 500;
    font-size: 44px; letter-spacing: 2px; color: var(--ink); line-height: 1;
  }

  .accent { position: absolute; width: 30px; height: 30px; }
  .accent-cyan { left: 353px; top: 152px; background: var(--cyan); }
  .accent-white { left: 400px; top: 152px; background: var(--white); box-shadow: 2px 2px 3px rgba(0,0,0,.25); }
  .accent-purple { left: 269px; top: 273px; background: var(--purple); }

  .contact-list {
    position: absolute; left: 44px; top: 240px; list-style: none;
    font-size: 14px; color: var(--ink-soft); line-height: 19px;
  }
  .contact-list li { display: flex; align-items: center; gap: 8px; }
  .contact-list svg { width: 13px; height: 13px; flex: none; }

  .person {
    position: absolute; left: 420px; top: 245px; width: 145px; text-align: center;
    color: var(--white);
  }
  .person-name {
    font-family: "Roboto Condensed", Arial, sans-serif; font-weight: 500; font-size: 20px; line-height: 24px;
  }
  .person-role {
    font-family: "Roboto", Arial, sans-serif; font-weight: 500; font-size: 14px; line-height: 20px;
  }

  .brand-back {
    left: 0; right: 0; top: 142px; justify-content: center;
  }
  .brand-back .brand-mark { background: var(--cyan); }
  .brand-back .brand-name { color: var(--white); }

  .back-url {
    position: absolute; left: 0; right: 0; top: 283px; text-align: center;
    font-size: 14px; letter-spacing: 5.5px; color: var(--muted-white);
  }
</style>
</head>
<body>
<main class="canvas">
  <section class="card card-front" aria-label="Card front">
    <svg class="corner-shape" width="600" height="343" viewBox="0 0 600 343" aria-hidden="true">
      <path fill="var(--cyan)" d="M600 137 L555 93 Q520 62 480 90 L350 230 Q330 258 350 285 L408 343 L600 343 Z"/>
    </svg>

    <div class="brand brand-front">
      <span class="brand-name">Quorvex</span>
      <span class="brand-mark"></span>
    </div>

    <span class="accent accent-cyan"></span>
    <span class="accent accent-white"></span>
    <span class="accent accent-purple"></span>

    <ul class="contact-list">
      <li>
        <svg viewBox="0 0 24 24" aria-hidden="true"><path fill="var(--purple)" d="M6.6 10.8a15 15 0 0 0 6.6 6.6l2.2-2.2c.3-.3.7-.4 1-.2 1.1.4 2.3.6 3.6.6.6 0 1 .4 1 1V20c0 .6-.4 1-1 1A17 17 0 0 1 3 4c0-.6.4-1 1-1h3.5c.6 0 1 .4 1 1 0 1.3.2 2.5.6 3.6.1.3 0 .7-.2 1z"/></svg>
        <span>555 210 4830</span>
      </li>
      <li>
        <svg viewBox="0 0 24 24" aria-hidden="true"><rect x="2" y="5" width="20" height="14" fill="var(--purple)"/><path d="M3 6l9 7 9-7" fill="none" stroke="var(--card-white)" stroke-width="1.8"/></svg>
        <span>dana@quorvexmail.com</span>
      </li>
      <li>
        <svg viewBox="0 0 24 24" aria-hidden="true"><circle cx="12" cy="12" r="10" fill="var(--purple)"/><path d="M2 12h20M12 2c3 3 3 17 0 20M12 2c-3 3-3 17 0 20" fill="none" stroke="var(--card-white)" stroke-width="1.4"/></svg>
        <span>www.quorvexmail.com</span>
      </li>
    </ul>

    <div class="person">
      <p class="person-name">DANA WHITLOW</p>
      <p class="person-role">CEO/FOUNDER</p>
    </div>
  </section>

  <section class="card card-back" aria-label="Card back">
    <div class="brand brand-back">
      <span class="brand-mark"></span>
      <span class="brand-name">Quorvex</span>
    </div>
    <p class="back-url">www.quorvexmail.com</p>
  </section>
</main>
</body>
</html>
```